Events By Halvane

Weddings, Corporate, Special Events
Memorable Catering, Personalized Menus, Custom Layout & Designs
Professional Staff, Excellent Service
Our Mission is Turning YOUR Vision into a Reality

Odette Halvane, Principal Planner
ph. 202 418-7352 - fax 301-847-2951
Email - eventsbyhalvane@mailtrove.com
Web - www.cateringbyhalvane.com
cateringbyhalvane@Snapverse

Target Market(s)

All Brides, Corprate Business, Special Events

Industry/Entity Type

Hospitality

Contact Information for Business Card

clean but affective

Font styles to use
Serif
Sans Serif
Script

Colors

Designer to choose colors to be used in the design.

Requirements
Must have
• logo with tagline using colors that will enhance what
• some pictures of nice table scape, hors d'oevures, upscale foods......
Nice to have
• Event: Something that happens or is regarded as happening, an occurrence especially one of some importance.
Should not have
• Use Logo on both sides

```html
<!DOCTYPE html>
<html lang="en">
<head>
<meta charset="utf-8">
<title>Events By Halvane – Business Card</title>
<link rel="stylesheet" href="https://fonts.googleapis.com/css2?family=Cinzel:wght@400;500&family=Open+Sans:wght@400&display=swap">
<style>
  :root {
    --bg: #2b2b2d;
    --card-dark: #151517;
    --card-light: #f4f4f5;
    --teal: #1fa9b4;
    --teal-soft: #37b7c0;
    --grey-ring: #9a9a9e;
    --ink: #555559;
  }
  * { margin: 0; padding: 0; box-sizing: border-box; }
  html, body { width: 1200px; height: 716px; overflow: hidden; background: var(--bg); }
  .canvas { position: relative; width: 1200px; height: 716px; }

  .card {
    position: absolute; top: 208px; width: 525px; height: 300px;
    border-radius: 18px; overflow: hidden;
  }
  .card--front { left: 50px; background: var(--card-dark); }
  .card--back  { left: 625px; background: var(--card-light); }

  .brand { position: absolute; text-align: center; }
  .brand__ring {
    display: block; margin: 0 auto; border-radius: 50%;
    border: 3px solid var(--grey-ring);
  }
  .brand__name {
    font-family: 'Cinzel', serif; font-weight: 500; color: var(--teal);
    letter-spacing: 0.5px; white-space: nowrap;
  }
  .brand__tagline {
    font-family: 'Cinzel', serif; font-weight: 400; white-space: nowrap;
    letter-spacing: 0.4px;
  }

  .card--front .brand { left: 0; right: 0; top: 52px; }
  .card--front .brand__ring { width: 70px; height: 70px; }
  .card--front .brand__name { font-size: 30px; margin-top: 10px; }
  .card--front .brand__tagline { font-size: 10px; color: #b8b8bc; margin-top: 4px; }
  .mission {
    position: absolute; left: 0; right: 0; top: 212px; text-align: center;
    font-family: 'Cinzel', serif; font-size: 13px; color: var(--teal);
    letter-spacing: 0.6px;
  }

  .card--back .brand { left: 30px; top: 84px; width: 220px; }
  .card--back .brand__ring { width: 56px; height: 56px; }
  .card--back .brand__name { font-size: 21px; margin-top: 8px; }
  .card--back .brand__tagline { font-size: 7.5px; color: #77777b; margin-top: 3px; }

  .contact { position: absolute; left: 268px; top: 70px; }
  .contact__name {
    font-family: 'Cinzel', serif; font-size: 21px; color: var(--ink); letter-spacing: 0.5px;
  }
  .contact__role {
    font-family: 'Cinzel', serif; font-size: 13px; color: var(--teal); letter-spacing: 0.8px;
    margin-bottom: 12px;
  }
  .contact__list { list-style: none; }
  .contact__item {
    display: flex; align-items: center; gap: 8px; height: 22px;
    font-family: 'Open Sans', sans-serif; font-size: 13px; color: var(--ink);
    white-space: nowrap;
  }
  .contact__icon { width: 12px; height: 12px; flex: none; }
</style>
</head>
<body>
<main class="canvas">

  <section class="card card--front" aria-label="Card front">
    <div class="brand">
      <span class="brand__ring"></span>
      <div class="brand__name">Events By Halvane</div>
      <div class="brand__tagline">Events Designed with You in Mind</div>
    </div>
    <p class="mission">Our Mission is Turning Your Vision into a Reality</p>
  </section>

  <section class="card card--back" aria-label="Card back">
    <div class="brand">
      <span class="brand__ring"></span>
      <div class="brand__name">Events By Halvane</div>
      <div class="brand__tagline">Events Designed with You in Mind</div>
    </div>

    <div class="contact">
      <div class="contact__name">Odette Halvane</div>
      <div class="contact__role">Principal Planner</div>
      <ul class="contact__list">
        <li class="contact__item">
          <svg class="contact__icon" viewBox="0 0 12 12"><path d="M2.5 1l2 2.3-1 1.3a7 7 0 0 0 3.9 3.9l1.3-1L11 9.5 9.6 11C5 11 1 7 1 2.4z" fill="var(--teal)"/></svg>
          202 418-7352
        </li>
        <li class="contact__item">
          <svg class="contact__icon" viewBox="0 0 12 12"><rect x="3" y="1" width="6" height="3" fill="var(--teal)"/><rect x="1" y="4.5" width="10" height="6.5" rx="1" fill="var(--teal)"/></svg>
          301-847-2951
        </li>
        <li class="contact__item">
          <svg class="contact__icon" viewBox="0 0 12 12"><rect x="1" y="2.5" width="10" height="7" fill="var(--teal)"/><path d="M1 2.5l5 4 5-4" stroke="#fff" fill="none"/></svg>
          www.cateringbyhalvane.com
        </li>
        <li class="contact__item">
          <svg class="contact__icon" viewBox="0 0 12 12" fill="none" stroke="var(--teal)" stroke-width="1.1"><circle cx="6" cy="6" r="5"/><ellipse cx="6" cy="6" rx="2.2" ry="5"/><path d="M1 6h10"/></svg>
          eventsbyhalvane@mailtrove.com
        </li>
        <li class="contact__item">
          <svg class="contact__icon" viewBox="0 0 12 12"><rect x="1" y="1" width="10" height="10" rx="2" fill="var(--teal)"/></svg>
          cateringbyhalvane@Snapverse
        </li>
      </ul>
    </div>
  </section>

</main>
</body>
</html>
```